Marrowick Billboards

We already hava a logo, slogan and general theme, we are looking for 2 to 3 billboard designs for out Recreational-Use Retail Cannabis Dispensary in NY state. We would like for the billboard to be a "Space" theme with a realistic-looking astronaut, we cannot have any "cartoon-like" images that would be attractive to children per state regulations. We would like the following wording included:
Marrowick Cannabis Company - Oswego , slogan is "Products out of this world" , address of 871 Tallow Lane - Oswego, Free Delivery - Orders over $150 . Our primary brand color is lime green.

```html
<!DOCTYPE html>
<html lang="en">
<head>
<meta charset="utf-8">
<title>Marrowick Cannabis Company Billboard</title>
<link rel="stylesheet" href="https://fonts.googleapis.com/css2?family=Anton&family=Cinzel:wght@500&family=Poppins:wght@700&display=swap">
<style>
  :root {
    --page: #2b3338;
    --lime: #c4dc2a;
    --lime-deep: #8a9a1c;
    --olive: #4a5418;
    --space: #0d0f0c;
    --maroon: #2a0e0e;
    --white: #ffffff;
    --ink: #14160f;
  }
  html, body {
    margin: 0;
    width: 1200px;
    height: 857px;
    overflow: hidden;
    background: var(--page);
  }
  .billboard {
    position: absolute;
    left: 0;
    top: 128px;
    width: 1200px;
    height: 600px;
    overflow: hidden;
    background: var(--space);
  }
  .space-scene {
    position: absolute;
    inset: 0;
    background:
      radial-gradient(ellipse 260px 320px at 260px 260px, rgba(196,220,42,0.55), transparent 70%),
      linear-gradient(100deg, var(--lime-deep) 0%, var(--olive) 30%, #1b1f0e 55%, var(--space) 75%, var(--maroon) 100%);
  }
  .astronaut {
    position: absolute;
    left: 80px;
    top: 110px;
    width: 310px;
    height: 490px;
    border-radius: 120px 120px 20px 20px;
    background: linear-gradient(180deg, #6f7a2a 0%, #4c5520 60%, #343b16 100%);
    opacity: 0.85;
  }
  .brand {
    position: absolute;
    left: 520px;
    top: 36px;
    width: 480px;
    text-align: center;
    font-family: "Cinzel", serif;
    font-weight: 500;
    color: var(--white);
    font-size: 26px;
    line-height: 1.05;
    letter-spacing: 1px;
  }
  .slogan {
    position: absolute;
    left: 390px;
    top: 112px;
    width: 760px;
    margin: 0;
    text-align: center;
    font-family: "Anton", sans-serif;
    font-weight: 400;
    font-size: 96px;
    line-height: 100px;
    color: var(--white);
    text-transform: uppercase;
    -webkit-text-stroke: 8px var(--ink);
    paint-order: stroke fill;
    letter-spacing: 1px;
  }
  .address-band {
    position: absolute;
    left: 390px;
    top: 332px;
    width: 810px;
    height: 54px;
    background: var(--lime);
  }
  .address {
    position: absolute;
    left: 390px;
    top: 332px;
    width: 760px;
    height: 54px;
    line-height: 54px;
    text-align: center;
    font-family: "Cinzel", serif;
    font-weight: 500;
    font-size: 30px;
    letter-spacing: 5px;
    color: var(--ink);
  }
  .offer {
    position: absolute;
    left: 390px;
    top: 410px;
    width: 760px;
    text-align: center;
    font-family: "Poppins", sans-serif;
    font-weight: 700;
    text-transform: uppercase;
  }
  .offer-title {
    display: block;
    font-size: 50px;
    line-height: 62px;
    color: var(--white);
  }
  .offer-terms {
    display: block;
    font-size: 58px;
    line-height: 70px;
    color: var(--lime);
  }
</style>
</head>
<body>
  <main class="billboard">
    <div class="space-scene" role="img" aria-label="Starry space sky over a planet horizon, glowing lime green on the left and fading to dark"></div>
    <div class="astronaut" role="img" aria-label="Realistic astronaut in a full space suit and helmet, standing in lime-tinted light"></div>

    <div class="brand">MARROWICK<br>CANNABIS COMPANY</div>

    <h1 class="slogan">Products out of<br>this world</h1>

    <div class="address-band"></div>
    <div class="address">871 Tallow Lane - Oswego</div>

    <p class="offer">
      <span class="offer-title">Free Delivery</span>
      <span class="offer-terms">Orders over $150</span>
    </p>
  </main>
</body>
</html>
```